Pet product line, needs a label design

We are a pharmaceutical company focused on animal health. We have been in the Mexican and Central American market for 10 years. During this time we have developed our line for production animals (beef, poultry, dairy, pigs...) and now we want to develop a line for pets.
Our first product are some pills made of Yucca (Yucca schidigera) which helps the digestive system of cats and dogs improve, reducing gas production and diminishing the bad smell of the pet feces.
We are looking for a design that can represent our new product line using this new product as an example, its name is 'VENTORAN'. The brand umbrella is BQ Vita, I am attaching this logo.
We need an attractive and original design with a strong personality, capable of jumping to the eyes of the consumer (pet owner) and also attractive for the Veterinarian who will recommend the product.
We want to highlight the benefits of the product by developing icons to the three main claims of the product.
We hope you will find this project attractive and challenging!!

Target Market(s)

Pet owners (mainly dog and cat)

Veterinarians

Industry/Entity Type

Pharmaceutical

Requirements
Must have
• * Product name (VENTORAN)
* Label Information (added in a word document)
* Band umbrella logo BQ Vita
* GREAT DESIGN
* The design should be horizontal (5cm height and 13 cm width)
Nice to have
• Nice product name design

Icon designs for the following claims (in spanish):
+ Limpia el trato digestivo (Cleans the digestive tract)
+ Reduce los malos olores (Reduces odors)
+ Propicia la digestión completa (Promotes complete digestion)

```html
<!DOCTYPE html>
<html lang="es">
<head>
<meta charset="utf-8">
<title>VENTORAN – etiqueta</title>
<link rel="stylesheet" href="https://fonts.googleapis.com/css2?family=Arimo:wght@400;700&family=Marcellus&family=Tinos&display=swap">
<style>
  :root {
    --bg: #e4e7ea;
    --navy: #1b3f93;
    --blue: #2456b4;
    --blue-light: #3d7fd0;
    --yellow: #f5c51a;
    --orange: #e9a515;
    --green-dark: #2f8a2a;
    --green: #4fae3b;
    --green-light: #8ccc5a;
    --meadow-top: #a6cde6;
    --meadow-mid: #b9d79a;
    --meadow-low: #86b43e;
    --pets-top: #9a7550;
    --pets-low: #c49562;
    --chip: #49a3e0;
    --icon-ink: #6b6258;
    --white: #ffffff;
  }
  * { margin: 0; padding: 0; box-sizing: border-box; }
  html, body { width: 1200px; height: 789px; overflow: hidden; }
  body {
    background: var(--bg);
    font-family: "Arimo", Arial, sans-serif;
    position: relative;
  }
  .label {
    position: absolute;
    left: 40px; top: 179px;
    width: 1120px; height: 431px;
    background: var(--navy);
    overflow: hidden;
  }
  .claim-band {
    position: absolute;
    left: 0; top: 10px; width: 100%; height: 70px;
    background: linear-gradient(90deg, var(--yellow), var(--orange));
    display: flex; align-items: center;
    padding-left: 110px;
  }
  .claim-icon {
    position: absolute; left: 40px; top: 9px;
    width: 52px; height: 52px; border-radius: 50%;
    background: var(--white);
    display: flex; align-items: center; justify-content: center;
  }
  .claim-icon svg { width: 34px; height: 34px; }
  .claim-text {
    color: var(--white);
    font-size: 22px; line-height: 1.1;
  }
  .scene {
    position: absolute;
    left: 0; top: 86px; width: 100%; height: 232px;
    background: linear-gradient(180deg, var(--meadow-top), var(--meadow-mid) 50%, var(--meadow-low));
  }
  .pets {
    position: absolute;
    left: 20px; top: 86px; width: 260px; height: 232px;
    background: linear-gradient(180deg, var(--pets-top), var(--pets-low));
  }
  .name-plaque {
    position: absolute;
    left: 360px; top: 110px; width: 440px; height: 150px;
    border-radius: 28px / 60px;
    background: linear-gradient(180deg, var(--green-light), var(--green) 45%, var(--green-dark));
    border: 3px solid rgba(255,255,255,.55);
    display: flex; flex-direction: column; align-items: center; justify-content: center;
  }
  .product-name {
    font-family: "Marcellus", "Optima", serif;
    font-weight: 400;
    color: var(--white);
    font-size: 70px; letter-spacing: 2px; line-height: 1;
  }
  .product-tagline {
    font-family: "Tinos", "Times New Roman", serif;
    color: var(--white);
    font-size: 22px; margin-top: 10px;
  }
  .actives {
    position: absolute;
    left: 850px; top: 200px;
  }
  .actives-chip {
    background: var(--chip);
    border: 2px solid var(--white);
    border-radius: 5px;
    color: var(--white);
    font-family: "Tinos", serif;
    font-size: 18px; line-height: 1.1;
    padding: 5px 10px;
    width: 120px;
  }
  .actives-list {
    list-style: none; margin-top: 10px;
    color: var(--white); font-size: 13px; line-height: 1.45;
  }
  .actives-list li::before { content: "• "; }
  .benefits-band {
    position: absolute;
    left: 0; top: 318px; width: 100%; height: 113px;
    background: linear-gradient(180deg, var(--blue-light), var(--blue) 40%, var(--navy));
    padding: 12px 0 0 330px;
    color: var(--white);
  }
  .benefits-title { font-size: 24px; font-weight: 400; }
  .benefits-cols { display: flex; gap: 40px; margin-top: 6px; }
  .benefits-cols ul { list-style: none; font-size: 14px; line-height: 1.45; }
  .benefits-cols li::before { content: "• "; }
  .brand-tile {
    position: absolute;
    left: 0; top: 282px; width: 180px; height: 130px;
    background: var(--white);
    border-radius: 0 24px 24px 0;
    display: flex; align-items: center; justify-content: center; gap: 10px;
  }
  .brand-square { width: 18px; height: 18px; background: var(--navy); }
  .brand-name { color: var(--navy); font-size: 30px; font-weight: 700; }
</style>
</head>
<body>
  <div class="label">
    <div class="claim-band">
      <span class="claim-icon">
        <svg viewBox="0 0 34 34" aria-hidden="true">
          <path d="M11 4 q-3 3 0 6 q3 3 0 6" fill="none" stroke="var(--icon-ink)" stroke-width="2" stroke-linecap="round"/>
          <path d="M17 2 q-3 3 0 6 q3 3 0 6" fill="none" stroke="var(--icon-ink)" stroke-width="2" stroke-linecap="round"/>
          <path d="M23 4 q-3 3 0 6 q3 3 0 6" fill="none" stroke="var(--icon-ink)" stroke-width="2" stroke-linecap="round"/>
          <path d="M6 31 q0 -5 5 -6 q0 -4 6 -5 q6 1 6 5 q5 1 5 6 z" fill="var(--icon-ink)"/>
        </svg>
      </span>
      <p class="claim-text">Reduce significativamente los malos olores<br>en los desechos de las mascotas</p>
    </div>

    <div class="scene" role="img" aria-label="Sunny meadow under a blue sky"></div>
    <div class="pets" role="img" aria-label="Photo of a German shepherd dog and an orange cat sitting together"></div>

    <div class="name-plaque">
      <h1 class="product-name">VENTORAN</h1>
      <p class="product-tagline">Con extracto natural de yuca</p>
    </div>

    <div class="actives">
      <div class="actives-chip">Ingredientes<br>Activos</div>
      <ul class="actives-list">
        <li>saponinas</li>
        <li>glicocompuestos</li>
      </ul>
    </div>

    <div class="benefits-band">
      <h2 class="benefits-title">Efectos benéficos en tu mascota</h2>
      <div class="benefits-cols">
        <ul>
          <li>Reduce el estrés</li>
          <li>Limpia el tracto digestivo</li>
          <li>Propicia una digestión completa</li>
        </ul>
        <ul>
          <li>Efectos antiinflamatorios</li>
          <li>Efectos antitumorales</li>
        </ul>
      </div>
    </div>

    <div class="brand-tile">
      <span class="brand-square"></span>
      <span class="brand-name">BQ Vita</span>
    </div>
  </div>
</body>
</html>
```